Brightwell Cleaning Services - Redesign

I've got my website designed a few years ago and it looks dated now. I would like to get a modern, happy, bright, and clean look. All the content needed can be found at my current website www.brightwellhq.example. Not necessarily need to use all of it, since I want something more clean and easy to read.
I need a 5 pages website:
HOME | SERVICES | ESTIMATE |TESTIMONIALS | CONTACT US

Industry/Entity Type

Janitorial Service

Number of Pages Required

5+ page

Colors
0792cd
34a6d7
85cae6
cee9f5
ebebeb
f0f0f0
f5f5f5
b1b1b1
000000

Requirements
Must have
• Who we are?
• Brightwell Cleaning Services is a local, family-owned, client-focused house and office cleaning company that strives to ensure the highest level of customer satisfaction. We offer expert residential and commercial cleaning services to all the Seattle and Eastside areas.
• Why Brightwell?
• √ We are insured, bonded and licensed.
•  Brightwell Cleaning Service is Fully Insured so you can rest easy knowing your home is protected.
•  Copy of insurance available upon request.
•

√ We provide all supplies and equipments needed to thoroughly clean your home or business.

• √ We are not a franchise. We are a local, family-owned company.

• When you call Brightwell Cleaning Services, you’ll always speak to one of the owners, which is a great benefit to you since this allows us to give you the personal attention and more time needed to clean your home the way you want it cleaned.

• √ We are good at what we do, and we like doing it.

```html
<!DOCTYPE html>
<html lang="en">
<head>
<meta charset="utf-8">
<title>Brightwell Cleaning Services</title>
<link href="https://fonts.googleapis.com/css2?family=Lato:wght@300;400;700&display=swap" rel="stylesheet">
<style>
:root{
  --blue:#0792cd;
  --blue-mid:#34a6d7;
  --blue-soft:#85cae6;
  --blue-pale:#cee9f5;
  --grey-1:#ebebeb;
  --grey-2:#f0f0f0;
  --grey-3:#f5f5f5;
  --grey-line:#b1b1b1;
  --ink:#000000;
  --text:#444;
  --muted:#777;
  --footer:#252525;
  --footer-bar:#ffffff;
}
*{margin:0;padding:0;box-sizing:border-box}
html,body{width:1200px;height:2586px;overflow:hidden}
body{font-family:'Lato',sans-serif;color:var(--text);background:#fff;position:relative}
.abs{position:absolute}

/* header */
.site-header{position:absolute;left:0;top:0;width:1200px;height:112px;background:#fff}
.brand{position:absolute;left:157px;top:30px;display:flex;align-items:center;gap:12px}
.brand-dot{width:26px;height:26px;border-radius:50%;background:var(--blue)}
.brand-name{font-size:38px;font-weight:700;color:var(--blue);letter-spacing:-0.5px}
.social-top{position:absolute;left:960px;top:22px;display:flex;gap:8px}
.social-top span{width:22px;height:22px;border-radius:50%;background:#8a8a8a}
.social-top span:first-child{background:var(--blue)}
.main-nav{position:absolute;left:536px;top:66px;display:flex;gap:10px;font-size:13px;letter-spacing:.8px}
.main-nav a{color:#333;text-decoration:none;padding:8px 15px;border-radius:16px}
.main-nav a.active{background:var(--blue);color:#fff}

/* hero */
.hero{position:absolute;left:0;top:112px;width:1200px;height:398px;
  background:linear-gradient(90deg,#3b4048 0%,#5d5c5a 35%,#6b5a48 65%,#4a3c30 100%)}
.hero-shade{position:absolute;inset:0;background:rgba(0,0,0,.25)}
.hero-title{position:absolute;left:0;width:1200px;top:142px;text-align:center;color:#fff;font-weight:700;font-size:30px;line-height:36px;letter-spacing:1px}
.hero-arrow{position:absolute;top:150px}

/* contact band */
.band{position:absolute;left:0;top:510px;width:1200px;height:96px;background:var(--blue);color:#fff}
.band-support{position:absolute;left:232px;top:24px}
.band-support h3{font-weight:400;font-size:21px}
.band-support p{font-size:13px;margin-top:4px}
.band-call{position:absolute;left:784px;top:24px}
.band-call h3{font-weight:400;font-size:21px;display:flex;align-items:center;gap:8px}
.band-call p{font-size:13px;margin-top:5px}

/* welcome */
.eyebrow{position:absolute;left:0;width:1200px;text-align:center;top:660px;font-size:13px;color:var(--blue);letter-spacing:1px}
.section-title{position:absolute;left:0;width:1200px;text-align:center;font-weight:300;color:#333}
.rule{position:absolute;height:2px;width:64px;left:568px;background:var(--grey-line)}
.service-hub{position:absolute;left:457px;top:782px;width:278px;height:278px;border-radius:50%;
  background:radial-gradient(circle,var(--blue-pale),#d8d8d8)}
.service-thumb{position:absolute;width:82px;height:82px;border-radius:50%;border:3px solid #fff;background:linear-gradient(135deg,#b9a58c,#6e6358)}
.service{position:absolute;width:300px}
.service h4{font-size:17px;font-weight:400;color:var(--blue);margin-bottom:6px}
.service p{font-size:13.5px;line-height:18px;color:var(--muted)}
.service.left{text-align:right}

/* why choose */
.who{position:absolute;left:0;top:1117px;width:1200px;height:310px;background:linear-gradient(90deg,var(--grey-2),var(--grey-1))}
.who-photo{position:absolute;left:157px;top:40px;width:279px;height:222px;background:linear-gradient(135deg,#c68a4c,#d9d9d9 55%,#8ec6e0)}
.who h2{position:absolute;left:462px;top:76px;font-weight:300;font-size:29px;color:#333}
.who .rule{left:462px;top:124px;width:40px}
.who p{position:absolute;left:462px;top:144px;width:565px;font-size:13.5px;line-height:19px;color:#555}

/* why brightwell */
.feature{position:absolute;width:360px}
.feature h4{font-size:16px;font-weight:400;color:#333;margin-bottom:8px}
.feature p{font-size:13px;line-height:18px;color:var(--muted)}
.feature-icon{position:absolute}
.divider-h{position:absolute;height:1px;background:#ddd}
.divider-v{position:absolute;width:1px;background:#ddd}

/* testimonials */
.testimonials{position:absolute;left:0;top:1860px;width:1200px;height:362px;background:var(--grey-3)}
.testimonial-photo{position:absolute;left:232px;top:112px;width:128px;height:128px;border-radius:50%;background:linear-gradient(160deg,#9fb1c4,#2d3a4a)}
.quote{position:absolute;left:425px;top:138px;width:500px;font-size:13.5px;line-height:19px;color:#444}
.quote-name{position:absolute;left:425px;top:262px;font-size:19px;color:#333}
.quote-meta{position:absolute;left:425px;top:290px;font-size:12px;color:#666}

/* footer */
.site-footer{position:absolute;left:0;top:2222px;width:1200px;height:302px;background:var(--footer);color:#ddd}
.footer-col{position:absolute;top:60px}
.footer-col h5{font-size:14px;font-weight:400;color:#fff;padding-bottom:12px;margin-bottom:14px;position:relative}
.footer-col h5::after{content:"";position:absolute;left:0;bottom:0;width:34px;height:1px;background:#666}
.footer-col ul{list-style:disc;padding-left:16px;font-size:12.5px;line-height:20px}
.footer-col li.current{color:var(--blue-mid)}
.cards{display:flex;flex-wrap:wrap;gap:8px;width:140px}
.cards span{width:40px;height:22px;background:#bfbfbf;border-radius:2px}
.footer-col p{font-size:12.5px;line-height:17px}
.newsletter-form{display:flex;margin-top:16px;width:255px;height:32px}
.newsletter-form .field{flex:1;border:1px solid #777;border-right:0;border-radius:3px 0 0 3px;padding:7px 10px;font-size:12.5px;color:#999;font-style:italic}
.newsletter-form .send{width:52px;background:var(--blue);border-radius:0 3px 3px 0;display:flex;align-items:center;justify-content:center}
.social-foot{display:flex;gap:8px;margin-top:16px}
.social-foot span{width:22px;height:22px;border-radius:50%;background:#8a8a8a}
.social-foot span:first-child{background:var(--blue)}
.copyright{position:absolute;left:0;top:2524px;width:1200px;height:62px;background:var(--footer-bar);text-align:center;line-height:62px;font-size:12px;color:#777}
</style>
</head>
<body>

<header class="site-header">
  <div class="brand"><span class="brand-dot"></span><span class="brand-name">Brightwell</span></div>
  <div class="social-top"><span></span><span></span><span></span></div>
  <nav class="main-nav">
    <a class="active">HOME</a><a>SERVICES</a><a>ESTIMATE</a><a>TESTIMONIALS</a><a>CONTACT US</a>
  </nav>
</header>

<section class="hero" role="img" aria-label="Photo of a bright modern office and living room interior">
  <div class="hero-shade"></div>
  <svg class="hero-arrow" style="left:168px" width="38" height="38" viewBox="0 0 38 38" fill="none" stroke="#fff" stroke-width="2"><path d="M14 4H34V34H14"/><path d="M26 19H4M11 12l-7 7 7 7"/></svg>
  <h1 class="hero-title">WE KEEP YOUR WORLD FRESH AND<br>SPARKLING CLEAN.</h1>
  <svg class="hero-arrow" style="left:1072px" width="38" height="38" viewBox="0 0 38 38" fill="none" stroke="var(--blue-mid)" stroke-width="2"><path d="M24 4H4V34H24"/><path d="M12 19H34M27 12l7 7-7 7"/></svg>
</section>

<section class="band">
  <svg class="abs" style="left:155px;top:24px" width="50" height="50" viewBox="0 0 50 50" fill="none" stroke="#fff" stroke-width="2.5"><circle cx="25" cy="25" r="22"/><path d="M16 14c-3 3-2 9 4 15s12 7 15 4l-4-5-4 2c-3-1-6-4-7-7l2-4z"/></svg>
  <div class="band-support">
    <h3>24/7 Customer Service &amp; Support</h3>
    <p>We are a local supplier in the community. We like to help you.</p>
  </div>
  <svg class="abs" style="left:688px;top:36px" width="16" height="26" viewBox="0 0 16 26" fill="none" stroke="#fff" stroke-width="2"><path d="M3 2l11 11L3 24"/></svg>
  <div class="band-call">
    <h3>Call Us
      <svg width="24" height="24" viewBox="0 0 24 24"><circle cx="12" cy="12" r="11" fill="#fff"/><path d="M8 6c-2 2-1 5 2 8s6 4 8 2l-2-3-2 1c-1-1-3-2-3-4l1-2z" fill="var(--blue)"/></svg>
      425-555-0142</h3>
    <p>info@brightwellhq.example</p>
  </div>
</section>

<p class="eyebrow">WELCOME TO BRIGHTWELL</p>
<h2 class="section-title" style="top:684px;font-size:29px">Commercial &amp; Residential Cleaning Services</h2>
<div class="rule" style="top:728px"></div>

<div class="service-hub" role="img" aria-label="Group photo of the cleaning team with company name"></div>
<div class="abs" style="left:457px;top:905px;width:278px;text-align:center;font-size:28px;font-weight:700;color:var(--blue)">Brightwell</div>
<div class="service-thumb" style="left:449px;top:786px" role="img" aria-label="Office interior photo"></div>
<div class="service-thumb" style="left:665px;top:786px" role="img" aria-label="Living room photo"></div>
<div class="service-thumb" style="left:449px;top:959px" role="img" aria-label="Empty room photo"></div>
<div class="service-thumb" style="left:665px;top:959px" role="img" aria-label="Classroom photo"></div>

<div class="service left" style="left:132px;top:796px"><h4>Office Cleaning</h4><p>We clean large or small office buildings<br>sing and much more.</p></div>
<div class="service" style="left:766px;top:796px"><h4>Residential Cleaning</h4><p>Brightwell Cleaning Services offer top<br>quality homes and apartments.</p></div>
<div class="service left" style="left:132px;top:968px"><h4>Move Out/In Cleaning</h4><p>Are planning on selling your property,<br>Or your tenancy agreement.</p></div>
<div class="service" style="left:766px;top:968px"><h4>School/Daycare Cleaning</h4><p>BCS is capable of tracking recess project<br>work in a timely fashion.</p></div>

<section class="who">
  <div class="who-photo" role="img" aria-label="Photo of two cleaners wiping cabinets"></div>
  <h2>Why choose?</h2>
  <div class="rule"></div>
  <p>Brightwell Cleaning Services is a local, family-owned, client-focused house and office cleaning company that strives to ensure the highest level of customer satisfaction. We offer expert residential and commercial cleaning services to all the Seattle and Eastside areas</p>
</section>

<h2 class="section-title" style="top:1484px;font-size:29px">Why Brightwell?</h2>
<div class="rule" style="top:1530px;width:40px;left:580px"></div>

<div class="divider-v" style="left:599px;top:1560px;height:103px"></div>
<div class="divider-v" style="left:599px;top:1690px;height:105px"></div>
<div class="divider-h" style="left:202px;top:1676px;width:356px"></div>
<div class="divider-h" style="left:641px;top:1676px;width:376px"></div>

<svg class="feature-icon" style="left:200px;top:1580px" width="40" height="46" viewBox="0 0 40 46"><path d="M20 2L4 8v14c0 11 7 19 16 22 9-3 16-11 16-22V8z" fill="#3a3a3a"/><path d="M20 6v35c7-3 12-10 12-19V11z" fill="#888"/></svg>
<div class="feature" style="left:258px;top:1578px"><h4>Insured, Bonded &amp; Licensed</h4><p>Brightwell Cleaning Service is Fully Insured so<br>you can rest easy knowing your home is protected.</p></div>

<svg class="feature-icon" style="left:630px;top:1578px" width="48" height="52" viewBox="0 0 48 52" fill="var(--blue-mid)"><circle cx="18" cy="7" r="6"/><path d="M10 16h16l4 18H6z"/><rect x="12" y="34" width="4" height="14"/><rect x="20" y="34" width="4" height="14"/><rect x="36" y="8" width="3" height="36"/><path d="M31 44h13l-2 6h-9z"/></svg>
<div class="feature" style="left:696px;top:1578px"><h4>Provide all Supplies &amp; Equipments</h4><p>We provide all supplies and equipments<br>needed to thoroughly clean your home or<br>business.</p></div>

<svg class="feature-icon" style="left:198px;top:1704px" width="46" height="40" viewBox="0 0 46 40" fill="#3a3a3a"><path d="M23 2L2 20h6v18h30V20h6z"/><rect x="10" y="2" width="5" height="10"/><circle cx="18" cy="24" r="3" fill="#fff"/><rect x="15" y="28" width="6" height="10" fill="#fff"/><circle cx="29" cy="24" r="3" fill="#fff"/><rect x="26" y="28" width="6" height="10" fill="#fff"/></svg>
<div class="feature" style="left:258px;top:1710px"><h4>Local, Family-Owned Company</h4><p>Give you the personal attention and more time<br>needed to clean your home the way you want.</p></div>

<svg class="feature-icon" style="left:630px;top:1702px" width="44" height="48" viewBox="0 0 44 48" fill="#3a3a3a"><circle cx="24" cy="6" r="5"/><path d="M6 8l6 12 8-2v12l-8 14 4 2 10-14 6 14 4-2-6-16V16l10-8-3-3-12 9h-6L10 6z"/></svg>
<div class="feature" style="left:696px;top:1710px"><h4>Good at What we do &amp; Enjoy it</h4><p>We are good at what we do, and we like doing it.</p></div>

<section class="testimonials">
  <h2 class="section-title" style="top:36px;font-size:29px">Testimonials</h2>
  <div class="rule" style="top:82px;width:40px;left:580px"></div>
  <svg class="abs" style="left:155px;top:162px" width="30" height="30" viewBox="0 0 30 30" fill="none" stroke="#888" stroke-width="1.5"><circle cx="15" cy="15" r="13"/><path d="M22 15H8M13 10l-5 5 5 5"/></svg>
  <div class="testimonial-photo" role="img" aria-label="Portrait photo of the client"></div>
  <p class="quote">We were referred to Marcus at Corven by one of our suppliers who told me about their 12 hour funding. I was amazed to find out that not only were our rates outdated, but we have been waiting for our deposits for an unnecessary 2 extra days. Marcus who has been our rep since day ...</p>
  <p class="quote-name">— &nbsp;Helena M.</p>
  <p class="quote-meta">Northgate Supply &nbsp;/&nbsp; Tacoma, WA</p>
  <svg class="abs" style="left:1013px;top:162px" width="30" height="30" viewBox="0 0 30 30" fill="none" stroke="var(--blue-mid)" stroke-width="1.5"><circle cx="15" cy="15" r="13"/><path d="M8 15h14M17 10l5 5-5 5"/></svg>
</section>

<footer class="site-footer">
  <div class="footer-col" style="left:175px">
    <h5>User Stuff</h5>
    <ul><li>Home</li><li>Services</li><li class="current">Estimate</li><li>Testimonials</li><li>Contact Us</li></ul>
  </div>
  <div class="footer-col" style="left:343px">
    <h5>Safe Shopping</h5>
    <div class="cards"><span></span><span></span><span></span><span></span></div>
  </div>
  <div class="footer-col" style="left:535px">
    <h5>Newsletter</h5>
    <p>Subscribe us today to receive to updates on<br>the Latest News &amp; Special Offers !</p>
    <div class="newsletter-form">
      <div class="field">Your Email</div>
      <div class="send"><svg width="18" height="16" viewBox="0 0 18 16"><path d="M1 7L17 1 13 15 9 10z" fill="#fff"/></svg></div>
    </div>
    <div class="social-foot"><span></span><span></span><span></span></div>
  </div>
  <div class="footer-col" style="left:859px">
    <h5>Contact Us</h5>
    <p style="font-size:19px;line-height:24px;color:#fff">425-555-0142</p>
    <p>info@brightwellhq.example</p>
    <p style="margin-top:24px">Head Office<br>118 Alder Lane,<br>Harbor District, Seattle</p>
  </div>
</footer>

<div class="copyright">© 2016 All Rights Reserved Brightwell Cleaning Services</div>

</body>
</html>
```